Backflow Prevention Test Gauge Calibration Service

Our company, Northfield Valve Supply Company, specializes in backflow prevention, a backflow preventer is a valve on the public drinking water system that prevents contamination. Backflow preventers need to be tested annually using a backflow test gauge. A backflow test gauge is considered an instrument and is required to be tested and calibrated annually to ensure they are working accurately. We offer that service, along with repair services if the instrument is damaged, and we refer to it as a "Hassle Free" service. We schedule the service for them once they provide their information and then email them a shipping label that they can print out, tape on their box and send the package from their business or home. We have a quick-turnaround time for this service because we understand how important this piece of equipment is for our customers to continue their job.

The main points we want to highlight on the flyer are:
* Hassle free shipping
* 1-Day turnaround time
* Service all gauge models
* Price includes incoming & return freight
* Honor all manufacturer warranties

We would like to include the manufacturers' logos and photos of the gauges that our customers use and will recognize (photos in brief).

There are two ways to schedule this service with us. They can call us at (800) 642-3871 or they can fill out a form on our website www.pipeguardshop.com.

Our text preferences are Myriad Pro and Tahoma. Our brand colors are red, white and blue. Please visit our website to get an idea of our style too.

```html
<!DOCTYPE html>
<html lang="en">
<head>
<meta charset="utf-8">
<title>Backflow Prevention Test Gauge Calibration Service</title>
<link href="https://fonts.googleapis.com/css2?family=Oswald:wght@500;600&family=Source+Sans+3:wght@400;600;700&display=swap" rel="stylesheet">
<style>
  :root{
    --blue:#1565b0;
    --blue-deep:#0c4f97;
    --blue-light:#cfe0f2;
    --red:#e4232b;
    --white:#ffffff;
    --ink:#2a2a2a;
    --grey:#c9c9c9;
    --page:#e6e6e6;
  }
  *{margin:0;padding:0;box-sizing:border-box}
  html,body{width:1200px;height:2301px;overflow:hidden;background:var(--page)}
  body{font-family:"Source Sans 3",Tahoma,sans-serif;color:var(--ink)}
  .flyer{position:absolute;left:80px;top:413px;width:1040px;height:1475px;background:var(--white);overflow:hidden;box-shadow:0 2px 10px rgba(0,0,0,.15)}
  .flyer-shapes{position:absolute;inset:0;width:1040px;height:1475px}
  .brand{position:absolute;left:548px;top:112px;display:flex;align-items:center;gap:12px;font-size:30px;font-weight:600;color:var(--blue)}
  .brand-mark{width:30px;height:30px;background:var(--red)}
  .headline{position:absolute;right:53px;text-align:right;font-family:"Oswald","Arial Narrow",sans-serif;font-weight:600;line-height:1;text-transform:uppercase}
  .headline-main{top:305px;font-size:106px;color:var(--red);letter-spacing:-1px}
  .headline-sub{color:var(--white);font-size:54px}
  .headline-sub.one{top:418px}
  .headline-sub.two{top:482px}
  .headline-rule{position:absolute;left:559px;top:560px;width:428px;height:3px;background:var(--white)}
  .headline-rule span{position:absolute;left:298px;top:-1px;width:60px;height:5px;background:var(--red)}
  .intro{position:absolute;left:559px;top:586px;width:428px;font-size:12px;line-height:17px;color:var(--white);text-align:justify;text-align-last:right}
  .gauge{position:absolute;left:697px;width:289px;height:126px;border:3px solid var(--blue);border-radius:9px;background:linear-gradient(135deg,#f4f4f4,#bdbdbd);}
  .section-title{position:absolute;left:56px;font-size:23px;font-weight:700;color:var(--blue);text-transform:uppercase}
  .section-title b{color:var(--red);font-weight:700;border-bottom:3px solid var(--red)}
  .services{top:948px}
  .partners{top:1254px}
  .service{position:absolute;display:flex;align-items:center;gap:26px;font-size:17px;font-weight:600;line-height:1.15;color:var(--ink)}
  .service-icon{width:54px;height:54px;flex:none}
  .partner-box{position:absolute;left:56px;top:1292px;width:516px;height:73px;border:2px solid var(--grey);display:flex;align-items:center;justify-content:space-around;padding:0 18px}
  .partner-badge{width:100px;height:30px;border-radius:4px;background:#d4d4d4}
  .call{position:absolute;left:630px;top:1384px;display:flex;align-items:baseline;gap:20px}
  .call-label{font-size:32px;font-weight:700;color:var(--blue);text-transform:uppercase}
  .call-number{font-size:28px;color:#333}
  .contact{position:absolute;top:1419px;display:flex;align-items:center;gap:10px;font-size:16px;color:var(--white)}
  .contact svg{width:18px;height:18px}
  .contact.email{left:56px}
  .contact.web{left:306px}
</style>
</head>
<body>
<main class="flyer">
  <svg class="flyer-shapes" viewBox="0 0 782 1109" preserveAspectRatio="none">
    <defs>
      <linearGradient id="warehouse" x1="0" y1="0" x2="1" y2="1">
        <stop offset="0" stop-color="#b89a6e"/>
        <stop offset=".55" stop-color="#8a7458"/>
        <stop offset="1" stop-color="#5d5550"/>
      </linearGradient>
    </defs>
    <rect role="img" aria-label="Photo of a technician on an orange rolling ladder stocking boxed parts on warehouse shelves" x="0" y="0" width="560" height="695" fill="url(#warehouse)"/>
    <polygon points="320,0 782,0 782,185 410,185" fill="#ffffff"/>
    <polygon points="410,185 782,185 782,560 485,560 425,695 290,420" fill="#0f5ea9"/>
    <polygon points="430,185 782,185 782,560 500,560 440,690 330,420" fill="#1565b0"/>
    <polygon points="485,560 782,560 782,1109 0,1109 0,695 425,695" fill="#ffffff"/>
    <path d="M0,1058 L390,1058 C410,1058 418,1094 440,1094 L782,1094 L782,1109 L0,1109 Z" fill="#1565b0"/>
  </svg>

  <div class="brand"><span class="brand-mark"></span>Northfield Valve Supply Company</div>

  <h1>
    <span class="headline headline-main">Backflow</span>
    <span class="headline headline-sub one">Prevention Test Gauge</span>
    <span class="headline headline-sub two">Calibration Service</span>
  </h1>
  <div class="headline-rule"><span></span></div>
  <p class="intro">Our company, Northfield Valve Supply Company, specializes in backflow prevention, a backflow preventer is a valve on the public drinking water system that prevents contamination. Our company, Northfield Valve Supply Company, specializes in backflow prevention, a backflow preventer is a valve on the public drinking water system that prevents contamination.</p>

  <div class="gauge" style="top:761px" role="img" aria-label="Photo of a backflow test kit in a grey case with gauge and hoses"></div>
  <div class="gauge" style="top:910px" role="img" aria-label="Photo of an analog test gauge in an open black case"></div>
  <div class="gauge" style="top:1059px" role="img" aria-label="Photo of a differential pressure gauge with coloured hoses"></div>
  <div class="gauge" style="top:1208px" role="img" aria-label="Photo of a handheld digital backflow test gauge"></div>

  <h2 class="section-title services"><b>Our</b> Services</h2>

  <div class="service" style="left:57px;top:1004px">
    <svg class="service-icon" viewBox="0 0 54 54"><circle cx="27" cy="27" r="26" fill="var(--blue-light)"/><circle cx="27" cy="27" r="20" fill="var(--blue)"/><rect x="15" y="20" width="16" height="12" fill="none" stroke="#fff" stroke-width="2"/><path d="M31 24h5l3 4v4h-8z" fill="none" stroke="#fff" stroke-width="2"/><circle cx="20" cy="34" r="2" fill="#fff"/><circle cx="35" cy="34" r="2" fill="#fff"/></svg>
    <span>Hassle free shipping</span>
  </div>
  <div class="service" style="left:57px;top:1082px">
    <svg class="service-icon" viewBox="0 0 54 54"><circle cx="27" cy="27" r="26" fill="var(--blue-light)"/><circle cx="27" cy="27" r="20" fill="var(--blue)"/><path d="M27 16l10 5v12l-10 5-10-5V21z M17 21l10 5 10-5 M27 26v12" fill="none" stroke="#fff" stroke-width="2" stroke-linejoin="round"/></svg>
    <span>Service all gauge<br>models</span>
  </div>
  <div class="service" style="left:57px;top:1158px">
    <svg class="service-icon" viewBox="0 0 54 54"><circle cx="27" cy="27" r="26" fill="var(--blue-light)"/><circle cx="27" cy="27" r="20" fill="var(--blue)"/><circle cx="27" cy="24" r="8" fill="none" stroke="#fff" stroke-width="2"/><path d="M22 30l-3 9 5-2 3 4 0-9 M32 30l3 9-5-2-3 4" fill="none" stroke="#fff" stroke-width="2" stroke-linejoin="round"/></svg>
    <span>Honor all manufacturer<br>warranties</span>
  </div>
  <div class="service" style="left:340px;top:1004px">
    <svg class="service-icon" viewBox="0 0 54 54"><circle cx="27" cy="27" r="26" fill="var(--blue-light)"/><circle cx="27" cy="27" r="20" fill="var(--blue)"/><path d="M38 27a11 11 0 1 1-3.2-7.8" fill="none" stroke="#fff" stroke-width="2"/><path d="M35 14v6h-6" fill="none" stroke="#fff" stroke-width="2"/><text x="27" y="31" text-anchor="middle" font-size="10" font-weight="700" fill="#fff" font-family="Source Sans 3, sans-serif">24h</text></svg>
    <span>1-Day turnaround time</span>
  </div>
  <div class="service" style="left:340px;top:1082px">
    <svg class="service-icon" viewBox="0 0 54 54"><circle cx="27" cy="27" r="26" fill="var(--blue-light)"/><circle cx="27" cy="27" r="20" fill="var(--blue)"/><circle cx="27" cy="27" r="11" fill="none" stroke="#fff" stroke-width="2"/><rect x="21" y="22" width="12" height="10" fill="none" stroke="#fff" stroke-width="2"/></svg>
    <span>Price includes incoming<br>&amp; return freight</span>
  </div>

  <h2 class="section-title partners"><b>Our</b> Partners</h2>
  <div class="partner-box">
    <span class="partner-badge"></span>
    <span class="partner-badge"></span>
    <span class="partner-badge"></span>
    <span class="partner-badge"></span>
  </div>

  <div class="call"><span class="call-label">Call Us</span><span class="call-number">(800) 642-3871</span></div>

  <div class="contact email">
    <svg viewBox="0 0 18 18"><rect x="1" y="4" width="16" height="11" fill="none" stroke="#fff" stroke-width="1.6"/><path d="M1 4l8 6 8-6" fill="none" stroke="#fff" stroke-width="1.6"/></svg>
    <span>info@pipeguardshop.com.</span>
  </div>
  <div class="contact web">
    <svg viewBox="0 0 18 18"><circle cx="9" cy="9" r="7.5" fill="none" stroke="#fff" stroke-width="1.5"/><ellipse cx="9" cy="9" rx="3.5" ry="7.5" fill="none" stroke="#fff" stroke-width="1.3"/><path d="M1.5 9h15" stroke="#fff" stroke-width="1.3"/></svg>
    <span>pipeguardshop.com.</span>
  </div>
</main>
</body>
</html>
```